Therapist website

I need a sqaure space web design for my therapy practice. I need a home page, a services page with 4 subpages, an about me, an insurnace page, a contact page, an EMDR page

```html
<!DOCTYPE html>
<html lang="en">
<head>
<meta charset="utf-8">
<title>Linden Creek Family Counseling</title>
<link href="https://fonts.googleapis.com/css2?family=Open+Sans:wght@400;600;700&display=swap" rel="stylesheet">
<style>
:root{
  --teal:#2fa3ad;
  --teal-dark:#1f7f88;
  --ink:#333b40;
  --muted:#6b7378;
  --line:#d6dadc;
  --footer:#ececec;
  --white:#ffffff;
}
*{box-sizing:border-box;margin:0;padding:0}
html,body{width:1200px;height:2868px;overflow:hidden}
body{position:relative;background:var(--white);font-family:"Open Sans",sans-serif;color:var(--ink)}
.abs{position:absolute}

/* Hero */
.hero{left:72px;top:40px;width:1056px;height:620px;overflow:hidden}
.hero-photo{position:absolute;inset:0;background:linear-gradient(135deg,#8fb5c4 0%,#c59a82 35%,#a7773f 55%,#5f8a3b 80%,#3f6b2e 100%)}
.hero-shade{position:absolute;inset:0;background:linear-gradient(180deg,rgba(0,0,0,.25),rgba(0,0,0,.05) 40%,rgba(0,0,0,.2))}
.brand{position:absolute;left:28px;top:34px;display:flex;align-items:center;gap:10px;color:var(--white);font-weight:600;font-size:15px;letter-spacing:2px}
.brand-dot{width:14px;height:14px;border-radius:50%;background:var(--white)}
.main-nav{position:absolute;right:28px;top:44px;display:flex;gap:36px}
.main-nav a{color:var(--white);font-size:12px;font-weight:600;letter-spacing:1px;text-decoration:none}
.hero-title{position:absolute;left:0;right:0;top:272px;text-align:center;color:var(--white)}
.hero-title h1{font-size:60px;font-weight:700;letter-spacing:1px;line-height:1.2}
.hero-title p{font-size:22px;font-weight:400;letter-spacing:2px;margin-top:2px}
.dots{position:absolute;left:0;right:0;top:588px;display:flex;justify-content:center;gap:8px}
.dots span{width:8px;height:8px;border-radius:50%;background:rgba(255,255,255,.5)}
.dots span:first-child{background:var(--white)}

/* Tiles */
.tile{top:732px;width:332px;height:288px;display:flex;align-items:center;justify-content:center;color:var(--white);font-weight:700;font-size:20px;letter-spacing:1px}
.tile-services{left:72px;background:linear-gradient(160deg,#c9b8a4,#8a7a6c)}
.tile-insurance{left:436px;background:linear-gradient(180deg,#9ab3c6 0%,#aebdc2 55%,#6f9a48 100%)}
.tile-emdr{left:796px;background:linear-gradient(160deg,#9aa6ad 0%,#6f8596 50%,#3f4850 100%)}
.tile-label{position:relative}

/* About */
.about-logo{left:72px;top:1150px;width:380px;text-align:center;color:var(--teal);font-weight:600}
.about-logo .mark{width:60px;height:60px;border-radius:50%;background:var(--teal);margin:0 auto 14px}
.about-logo .name{font-size:46px;letter-spacing:1px;line-height:1}
.about-logo .sub{font-size:20px;letter-spacing:4px;margin-top:8px}
.about{left:520px;top:1114px;width:608px}
.about h2{font-size:24px;font-weight:600;letter-spacing:1px;color:var(--ink)}
.about p{margin-top:16px;font-size:13px;line-height:1.75;color:var(--muted)}
.btn-outline{display:inline-block;margin-top:22px;padding:14px 30px;border:2px solid var(--teal);color:var(--teal);font-size:13px;font-weight:600;letter-spacing:1px}

/* Banner */
.banner{left:72px;top:1452px;width:1056px;height:460px;overflow:hidden}
.banner-photo{position:absolute;inset:0;background:linear-gradient(180deg,#7d9aa6 0%,#b9b7a4 45%,#c9a86a 65%,#8c6e3f 100%)}
.banner-copy{position:absolute;left:0;right:0;top:175px;text-align:center;color:var(--white)}
.banner-copy h3{font-size:32px;font-weight:600}
.btn-ghost{display:inline-block;margin-top:20px;padding:12px 26px;border:2px solid var(--white);color:var(--white);font-size:12px;font-weight:600;letter-spacing:1px}

/* Location */
.address{left:72px;top:1984px;font-size:13px;color:var(--ink)}
.social-links{left:780px;top:1984px;font-size:13px;color:var(--ink)}
.map{left:72px;top:2028px;width:516px;height:340px;background:linear-gradient(150deg,#e7e5df,#dcdad2 60%,#e9e2c8)}
.gallery{left:608px;top:2028px;width:520px;height:340px;display:grid;grid-template-columns:repeat(3,1fr);grid-template-rows:repeat(2,1fr);gap:8px}
.gallery div:nth-child(1){background:linear-gradient(135deg,#c8a48b,#6e5a4c)}
.gallery div:nth-child(2){background:linear-gradient(135deg,#9ab0c0,#8a6c5a)}
.gallery div:nth-child(3){background:linear-gradient(180deg,#c5d7e2,#7f9a66)}
.gallery div:nth-child(4){background:linear-gradient(135deg,#b89078,#5b4a3e)}
.gallery div:nth-child(5){background:linear-gradient(135deg,#c2a68c,#7b8f72)}
.gallery div:nth-child(6){background:linear-gradient(135deg,#b7c6d0,#9a7a5c)}

/* Footer */
.footer{left:0;top:2472px;width:1200px;height:396px;background:var(--footer);text-align:center}
.footer h4{margin-top:56px;font-size:28px;font-weight:400;color:var(--ink)}
.footer .lead{margin-top:14px;font-size:13px;color:var(--muted)}
.signup{margin:22px auto 0;display:flex;width:392px;height:46px}
.signup .field{flex:1;background:var(--white);border:1px solid var(--line);font-size:13px;color:var(--muted);display:flex;align-items:center;padding-left:16px}
.signup .submit{width:92px;background:var(--teal);color:var(--white);font-size:13px;font-weight:600;display:flex;align-items:center;justify-content:center}
.footer-nav{margin-top:44px;display:flex;justify-content:center;gap:44px}
.footer-nav a{font-size:12px;font-weight:600;color:var(--ink);text-decoration:none;letter-spacing:1px}
.copyright{margin-top:18px;font-size:12px;color:var(--muted)}
.footer-social{margin-top:14px;display:flex;justify-content:center;gap:16px}
.footer-social span{width:18px;height:18px;border-radius:50%;background:var(--ink)}
</style>
</head>
<body>

<section class="hero abs">
  <div class="hero-photo" role="img" aria-label="Smiling family of four embracing outdoors"></div>
  <div class="hero-shade"></div>
  <div class="brand"><span class="brand-dot"></span>LINDEN CREEK</div>
  <nav class="main-nav">
    <a href="#">HOME</a><a href="#">SERVICES</a><a href="#">ABOUT</a><a href="#">INSURANCE</a><a href="#">EMDR</a><a href="#">CONTACT</a>
  </nav>
  <div class="hero-title">
    <h1>Linden Creek</h1>
    <p>FAMILY COUNSELING</p>
  </div>
  <div class="dots"><span></span><span></span><span></span><span></span></div>
</section>

<a class="tile tile-services abs" role="img" aria-label="Portrait of a smiling woman"><span class="tile-label">SERVICES</span></a>
<a class="tile tile-insurance abs" role="img" aria-label="Person relaxing with a laptop on grass"><span class="tile-label">INSURANCE</span></a>
<a class="tile tile-emdr abs" role="img" aria-label="Close-up photograph of an eye"><span class="tile-label">EMDR</span></a>

<div class="about-logo abs">
  <div class="mark"></div>
  <div class="name">LINDEN CREEK</div>
  <div class="sub">FAMILY COUNSELING</div>
</div>

<section class="about abs">
  <h2>ABOUT OUR COMPANY</h2>
  <p>Welcome to Linden Creek Family Counseling and thank you for visiting my website to learn more about whether I may be a good fit for your current life struggle. I value bringing my clients hope, encouragement and support, and working together to find the answers that bring relief and healing. I earned an M.S. in Clinical Psychology in 2004 and became licensed as a Marriage and Family Therapist in 2008.</p>
  <span class="btn-outline">READ MORE</span>
</section>

<section class="banner abs">
  <div class="banner-photo" role="img" aria-label="Woman raising her arms in a wheat field under an open sky"></div>
  <div class="banner-copy">
    <h3>Nam viverra arcu at magna</h3>
    <span class="btn-ghost">READ MORE</span>
  </div>
</section>

<div class="address abs">2450 Meadowbrook Lane Suite 210 Fairhaven, CA 90000</div>
<div class="social-links abs">Gallery &nbsp;/&nbsp; Community &nbsp;/&nbsp; Updates</div>

<div class="map abs" role="img" aria-label="Street map showing the office location"></div>
<div class="gallery abs">
  <div role="img" aria-label="Family photo"></div>
  <div role="img" aria-label="Couple with child"></div>
  <div role="img" aria-label="Child playing outdoors"></div>
  <div role="img" aria-label="Smiling children"></div>
  <div role="img" aria-label="Parent and child in a field"></div>
  <div role="img" aria-label="Young boy portrait"></div>
</div>

<footer class="footer abs">
  <h4>Subscribe Email</h4>
  <p class="lead">Subscribe to our mailing list to receive updates and promotional offers.</p>
  <div class="signup"><div class="field">Enter Email Address</div><div class="submit">SIGNUP</div></div>
  <nav class="footer-nav">
    <a href="#">HOME</a><a href="#">SERVICES</a><a href="#">ABOUT</a><a href="#">INSURANCE</a><a href="#">EMDR</a><a href="#">CONTACT</a>
  </nav>
  <p class="copyright">Copyright © 2016. Company Name All Rights Reserved</p>
  <div class="footer-social"><span></span><span></span><span></span><span></span><span></span></div>
</footer>

</body>
</html>
```